Small Web Design for Boat Industry

We are looking for a small 4 page web site. The designs will need to be clean and stylish. Please see samples of sites that we like.

http://www.veltrani.co.uk/
http://quillmarsh.com/

We need a quick turnaround.

Requirements
Must have
• Please see attached documents with all wording and images

```html
<!DOCTYPE html>
<html lang="en">
<head>
<meta charset="utf-8">
<title>Berthline – Boat Docking</title>
<link rel="stylesheet" href="https://fonts.googleapis.com/css2?family=Baumans&family=Lato:wght@300;400;700&display=swap">
<style>
:root{
  --red:#b0222c;
  --blue:#1f6aa8;
  --text-blue:#3d7cb8;
  --grey-text:#a8a8a8;
  --dark:#333;
  --light-bg:#f7f9fb;
  --testi-bg:#eceef0;
  --band-light:#7ba8cf;
  --band-dark:#2f78b2;
  --white:#fff;
}
*{margin:0;padding:0;box-sizing:border-box}
html,body{width:1200px;height:3025px;overflow:hidden}
body{position:relative;font-family:"Lato",sans-serif;font-weight:300;background:var(--white);color:var(--dark)}
.abs{position:absolute}
.display{font-family:"Baumans",cursive;font-weight:400}
.btn{position:absolute;display:flex;align-items:center;justify-content:center;background:var(--red);color:var(--white);border-radius:10px;font-size:23px;font-weight:300;letter-spacing:.5px;white-space:nowrap}

/* hero */
.hero{left:0;top:0;width:1200px;height:815px;background:radial-gradient(ellipse at 60% 40%,#f4f4f4 0%,#e2e2e2 60%,#cfcfcf 100%)}
.header{left:0;top:0;width:1200px;height:150px}
.brand{left:70px;top:44px;display:flex;align-items:center;gap:14px}
.brand-mark{width:30px;height:30px;background:var(--red)}
.brand-name{font-size:52px;font-weight:700;color:var(--red);letter-spacing:1px;line-height:1}
.cart{left:963px;top:20px;font-size:9px;font-weight:400;color:#555;display:flex;gap:6px;align-items:center;white-space:nowrap}
.cart-box{width:22px;height:14px;background:var(--red)}
.nav{left:567px;top:70px;width:580px;height:30px;font-size:19px;font-weight:400;color:var(--dark)}
.nav span{position:absolute;top:0;white-space:nowrap}
.hero-card{left:234px;top:245px;width:732px;height:415px;background:rgba(110,110,110,.72);border-radius:8px;text-align:center;color:var(--white)}
.hero-title{position:absolute;left:0;top:38px;width:100%;font-size:50px}
.hero-copy{position:absolute;left:40px;top:130px;width:652px;font-size:27px;line-height:35px;color:#ececec}
.slider-tab{left:524px;top:777px;width:152px;height:40px;background:var(--white);border-radius:10px 10px 0 0;display:flex;gap:10px;align-items:center;justify-content:center}
.dot{width:13px;height:13px;border-radius:50%;background:var(--blue)}
.dot.active{background:var(--red)}

/* product */
.product{left:0;top:815px;width:1200px;height:955px;background:var(--light-bg)}
.section-title{position:absolute;left:0;width:1200px;text-align:center;font-size:36px;color:var(--blue)}
.shot{position:absolute;width:258px;background:linear-gradient(135deg,#d9d9d9 0%,#6a6a6a 45%,#151515 100%)}
.feature-name{position:absolute;font-size:21px;color:var(--text-blue);font-weight:400;white-space:nowrap}
.feature-copy{position:absolute;width:250px;font-size:11.5px;line-height:15px;color:#999;font-weight:400}
.intro{left:96px;top:1372px;width:285px;font-size:22px;line-height:25px;color:var(--grey-text)}
.intro em{font-style:normal;color:var(--red)}

/* testimonials */
.testimonials{left:0;top:1770px;width:1200px;height:524px;background:var(--testi-bg)}
.quote{position:absolute;left:96px;width:820px;font-size:18px;line-height:25px;color:var(--grey-text)}
.quote-mark{font-size:24px;color:#999;margin-right:4px}
.quote-author{position:absolute;left:968px;font-size:22px;color:var(--text-blue);font-weight:400;white-space:nowrap}
.rule{position:absolute;left:96px;width:1006px;height:1px;background:#d4d6d8}

/* contact */
.contact-light{left:0;top:2488px;width:1200px;height:267px;background:var(--band-light)}
.contact-dark{left:0;top:2755px;width:1200px;height:270px;background:var(--band-dark)}
.field{position:absolute;left:103px;width:439px;background:var(--white);border-radius:8px;font-size:16px;font-weight:400;color:#555;padding:10px 24px}
.contact-title{left:600px;top:2578px;width:502px;text-align:right;font-size:38px;color:var(--white)}
.contact-lines{left:600px;top:2650px;width:502px;text-align:right;font-size:27px;line-height:31px;color:var(--white);font-style:normal}
.footer-rule{left:96px;top:2970px;width:1006px;height:1px;background:rgba(255,255,255,.45)}
.copyright{left:0;top:2995px;width:1200px;text-align:center;font-size:13px;font-weight:400;color:var(--white)}
</style>
</head>
<body>

<section class="abs hero" role="img" aria-label="Photo of a black foam docking pole with a metal ring on a light grey background"></section>

<header class="abs header">
  <div class="abs brand"><span class="brand-mark"></span><span class="brand-name">Berthline</span></div>
  <div class="abs cart">SHOPPING CART: 0 ITEMS <span class="cart-box"></span></div>
  <nav class="abs nav">
    <span style="left:0">Home</span>
    <span style="left:93px">Product</span>
    <span style="left:201px">FAQs</span>
    <span style="left:290px">Videos</span>
    <span style="left:381px">Buy now</span>
    <span style="left:487px">Contact us</span>
  </nav>
</header>

<div class="abs hero-card">
  <h1 class="display hero-title">Revolutionary Boat Fenders!</h1>
  <p class="hero-copy">Berthline is a new, fast and easy system for temporally docking boats reducing the need for fenders. Designed to keep boats off of docks, Berthline will impress you with how quickly you can connect your boat</p>
  <div class="btn" style="left:265px;top:322px;width:199px;height:58px">KNOW MORE</div>
</div>

<div class="abs slider-tab"><span class="dot active"></span><span class="dot"></span><span class="dot"></span><span class="dot"></span><span class="dot"></span></div>

<section class="abs product">
  <h2 class="display section-title" style="top:55px">The Product</h2>
</section>

<div class="shot" style="left:96px;top:976px;height:176px" role="img" aria-label="Photo of the docking pole close up"></div>
<div class="shot" style="left:471px;top:976px;height:176px" role="img" aria-label="Photo of two docking poles with rings"></div>
<div class="shot" style="left:845px;top:976px;height:176px" role="img" aria-label="Photo of the docking pole lying on a surface"></div>
<div class="feature-name" style="left:110px;top:1178px">Durable</div>
<div class="feature-name" style="left:487px;top:1178px">Efficient</div>
<div class="feature-name" style="left:862px;top:1178px">Sizeable</div>
<p class="feature-copy" style="left:110px;top:1224px">Lorem ipsum dolor sit amet adipiscing elit. Sed rhoncus faucibus faucibus. Maecenas erat odio mattis</p>
<p class="feature-copy" style="left:487px;top:1224px">Lorem ipsum dolor sit amet adipiscing elit. Sed rhoncus faucibus faucibus. Maecenas erat odio mattis</p>
<p class="feature-copy" style="left:862px;top:1224px">Lorem ipsum dolor sit amet adipiscing elit. Sed rhoncus faucibus faucibus. Maecenas erat odio mattis</p>

<p class="abs intro">Lorem ipsum dolor sit amet, consectur as piscing eli. <em>Sed rhoncus</em> faucibus faucibus. Maecenas erat odio, mattis id suscipit aidi, ullamorper nec felia. <em>Pellentesque ut</em> seme et ante condimentum ultric es</p>
<div class="btn" style="left:101px;top:1623px;width:196px;height:58px">SEE VIDEOS</div>

<div class="shot" style="left:471px;top:1376px;height:169px" role="img" aria-label="Photo of stacked docking poles"></div>
<div class="shot" style="left:845px;top:1376px;height:169px" role="img" aria-label="Photo of the docking pole side view"></div>
<div class="feature-name" style="left:489px;top:1579px">Fast</div>
<div class="feature-name" style="left:862px;top:1579px">Used in most docks</div>
<p class="feature-copy" style="left:487px;top:1625px">Lorem ipsum dolor sit amet adipiscing elit. Sed rhoncus faucibus faucibus. Maecenas erat odio mattis</p>
<p class="feature-copy" style="left:862px;top:1625px">Lorem ipsum dolor sit amet adipiscing elit. Sed rhoncus faucibus faucibus. Maecenas erat odio mattis</p>

<section class="abs testimonials">
  <h2 class="display section-title" style="top:62px">Client Testimonials</h2>
  <p class="quote" style="top:160px"><span class="quote-mark">“</span>Lorem ipsum dolor sit amet, consectur ais piscing eli. Sed rhoncus faucibus faucibus. Maecenas erat odio, mattis id suscipit aidi, ullamorper nec felia. Pellentesque ut seme et ante condimentum ultric es quis necolo”</p>
  <div class="quote-author" style="top:162px">Mr. Alan Reed</div>
  <div class="rule" style="top:292px"></div>
  <p class="quote" style="top:342px"><span class="quote-mark">“</span>Lorem ipsum dolor sit amet, consectur ais piscing eli. Sed rhoncus faucibus faucibus. Maecenas erat odio, mattis id suscipit aidi, ullamorper nec felia. Pellentesque ut seme et ante condimentum ultric es quis necolo lorem”</p>
  <div class="quote-author" style="top:352px">Nora Pike</div>
</section>

<div class="btn" style="left:461px;top:2360px;width:278px;height:68px">GET YOUR BERTHLINE</div>

<section class="abs contact-light"></section>
<section class="abs contact-dark"></section>
<div class="field" style="top:2574px;height:48px">Name</div>
<div class="field" style="top:2650px;height:171px">Message</div>
<div class="btn" style="left:431px;top:2864px;width:111px;height:50px">SEND</div>
<h2 class="abs display contact-title">Contact us</h2>
<address class="abs contact-lines">12 Harbour Lane<br>Westbay Victoria Australia 3190<br>+61 3 5550 1827<br>info@berthline.com</address>
<div class="abs footer-rule"></div>
<p class="abs copyright">Copyright 2013 Berthline. All Rights Reserved</p>

</body>
</html>
```